FINANCIAL ADVISOR WORDPRESS WEBSITE

Hello, Here% 26 # 39; s the project. I just want a copy of this website .. I https://www.groupe-valmoril.fr/lp/valmoril/gestion-patrimoine-azurel.php?wh=adwords%26amp;gclid=Xk4LTZbrQmFvWpNsEHdoRQjaBT-_K_R2M8TyVpDLZVH47Wu_GlxHxLnRfYq_83m-7TOeqW_H49J_lkcbNd5-VPTm_xkD just want you to make it work under wordpress as i can update easily. Please find the logo attached. If you can install it in my web host it would be great. Thanks Lucien.

Number of Pages Required

3 page

Font styles to use
Serif

Colors
1f66ae

Requirements
Must have
• WORDPRESS ONLY

```html
<!DOCTYPE html>
<html lang="en">
<head>
<meta charset="utf-8">
<title>Nerolia Patrimoine – Wealth management</title>
<link rel="stylesheet" href="https://fonts.googleapis.com/css2?family=Montserrat:wght@300;400;500;600&display=swap">
<style>
:root{
  --navy:#1f4f9c;
  --hero:#2a6ed6;
  --brand:#1f66ae;
  --ink:#2b2f38;
  --muted:#7a7f8a;
  --soft:#f3f5fb;
  --line:#e3e6ee;
  --green:#22c88e;
  --pie-dark:#3d4a5c;
  --pie-pink:#e94b7a;
  --pie-teal:#36b8c4;
}
*{box-sizing:border-box;margin:0;padding:0}
html,body{width:1200px;height:3780px;overflow:hidden}
body{font-family:'Montserrat',sans-serif;color:var(--ink);background:#fff;position:relative}
.abs{position:absolute}
/* header */
.site-header{position:absolute;left:0;top:0;width:1200px;height:64px;background:var(--navy);color:#fff}
.brand{position:absolute;left:92px;top:21px;font-size:17px;font-weight:500;line-height:22px}
.main-nav{position:absolute;right:92px;top:22px;display:flex;gap:49px;font-size:13px}
/* hero */
.hero{position:absolute;left:0;top:64px;width:1200px;height:665px;background:var(--hero);color:#fff;overflow:hidden}
.hero h1{position:absolute;left:92px;top:78px;font-size:19px;font-weight:500;line-height:24px;text-transform:uppercase;width:300px}
.hero .lead{position:absolute;left:92px;top:158px;font-size:12px;line-height:18px;width:400px}
.field{position:absolute;background:#fff;color:#555;font-size:12px;height:32px;padding:9px 12px}
.submit{position:absolute;left:92px;top:460px;width:385px;height:33px;background:var(--green);color:#fff;font-size:13px;text-align:center;line-height:33px}
.hero .fine{position:absolute;left:92px;top:508px;width:385px;text-align:center;font-size:10px;color:#cfe0ff}
.hero-art{position:absolute;left:528px;top:83px;width:640px;height:582px;border-radius:200px 200px 0 0;background:radial-gradient(circle at 50% 55%,#3a8ae8 0%,#1e55b8 60%,#163f90 100%)}
/* advantages */
.advantages{position:absolute;left:0;top:729px;width:1200px;height:653px;background:var(--soft)}
.section-title{position:absolute;left:0;width:1200px;text-align:center;font-size:29px;font-weight:500;line-height:37px}
.section-lead{position:absolute;left:320px;width:560px;text-align:center;font-size:13.5px;line-height:20px;color:#555}
.card{position:absolute;width:323px;height:143px;background:#fff;box-shadow:0 2px 8px rgba(0,0,0,.07)}
.card svg{position:absolute;left:16px;top:26px}
.card h3{position:absolute;left:83px;top:24px;font-size:16.5px;font-weight:400;line-height:20px;width:220px}
.card p{position:absolute;left:83px;font-size:12px;line-height:19px;color:var(--muted);width:200px}
/* pinel */
.pinel{position:absolute;left:0;top:1382px;width:1200px;height:599px;background:#fff}
.chart-card{position:absolute;left:92px;top:210px;width:502px;height:301px;background:#fff;box-shadow:0 2px 10px rgba(0,0,0,.1)}
.legend{position:absolute;left:308px;font-size:7px;color:#333;display:flex;align-items:center;gap:6px}
.legend i{width:10px;height:10px;border-radius:50%;display:inline-block}
.chart-caption{position:absolute;left:0;top:258px;width:502px;text-align:center;font-size:12.5px;font-weight:500}
.footnote{position:absolute;left:92px;top:517px;width:1016px;font-size:7px;line-height:11px;font-style:italic;color:#888}
.focus{position:absolute;left:633px;top:206px;width:460px}
.focus .kicker{font-size:21px;font-weight:300;color:#555}
.focus h2{font-size:25px;font-weight:500;margin-top:2px}
.focus p{font-size:13px;line-height:21px;color:#555;margin-top:20px}
.focus p+p{margin-top:10px}
.btn{display:inline-block;background:var(--brand);color:#fff;font-size:13px;padding:9px 20px;margin-top:20px}
/* testimonials */
.testimonials{position:absolute;left:0;top:1981px;width:1200px;height:509px;background:linear-gradient(160deg,#3a4656 0%,#2a3442 60%,#333f4e 100%);color:#fff}
.testimonials .section-title{top:73px;color:#fff}
.testimonials .sub{position:absolute;left:0;top:122px;width:1200px;text-align:center;font-size:12.5px;color:#aab3c0}
.quote{position:absolute;font-size:13px;line-height:22px;text-align:center}
.quote-box{position:absolute;left:431px;top:162px;width:338px;height:192px;background:#2e72d6}
.avatar{position:absolute;left:572px;top:324px;width:56px;height:56px;border-radius:50%;background:linear-gradient(#c9d0da,#8c97a6);border:3px solid #fff}
.author{position:absolute;left:0;top:392px;width:1200px;text-align:center;font-size:13px;font-weight:600}
.dots{position:absolute;left:586px;top:424px;display:flex;gap:5px}
.dots i{width:5px;height:5px;border-radius:50%;background:#fff}
.dots i:first-child{background:#4c8df0}
/* group */
.group{position:absolute;left:0;top:2490px;width:1200px;height:438px;background:linear-gradient(100deg,#1f5fc4,#2f7de0);color:#fff;overflow:hidden}
.group h2{position:absolute;left:94px;top:70px;font-size:26px;font-weight:500;line-height:35px;width:440px}
.group p{position:absolute;left:92px;font-size:15px;line-height:20px}
.badge{position:absolute;top:307px;height:58px;background:#fff;border:3px solid #d0202a}
.group-photo{position:absolute;left:675px;top:30px;width:352px;height:408px;border-radius:170px 170px 0 0;background:linear-gradient(#8aa9d8,#3d6fbf)}
/* figures */
.figure{position:absolute;top:2962px;display:flex;gap:14px;align-items:center}
.figure b{display:block;font-size:17px;font-weight:400}
.figure span{font-size:12px;color:#555}
.divider{position:absolute;left:92px;top:3045px;width:1016px;height:1px;background:var(--line)}
.value-pill{position:absolute;left:536px;top:3110px;width:128px;height:34px;border-radius:17px;background:var(--brand);color:#fff;font-size:13px;font-weight:600;text-align:center;line-height:34px}
.value-card{position:absolute;top:3254px;width:245px;height:151px;color:#fff;padding:32px 48px}
.value-card h3{font-size:16px;font-weight:500}
.value-card p{font-size:12px;line-height:17px;margin-top:14px;opacity:.9}
/* footer */
.site-footer{position:absolute;left:0;top:3493px;width:1200px;height:287px;background:var(--soft)}
.contact{position:absolute;top:78px;display:flex;align-items:center;gap:12px;font-size:15px;color:#444}
.social{position:absolute;left:871px;top:80px;display:flex;gap:18px}
.social i{width:20px;height:20px;background:var(--brand);border-radius:3px}
.legal{position:absolute;left:92px;top:146px;width:1016px;font-size:9px;line-height:16px;color:#777}
.to-top{position:absolute;left:1044px;top:219px;width:54px;height:54px;border-radius:50%;background:var(--brand)}
</style>
</head>
<body>

<header class="site-header">
  <div class="brand">Nerolia Patrimoine</div>
  <nav class="main-nav"><span>Tax exemption</span><span>Pinel Law</span><span>Testimonials</span><span>Key figures</span><span>Our values</span></nav>
</header>

<section class="hero">
  <h1>For the management of your wealth, trust a champion!</h1>
  <p class="lead">Benefit from a free and non-binding balance sheet, to find out what tax reduction you are entitled to</p>
  <div class="field" style="left:92px;top:219px;width:182px">Tax bracket</div>
  <div class="field" style="left:297px;top:219px;width:180px">Year of birth</div>
  <div class="field" style="left:92px;top:266px;width:385px">Address Email</div>
  <div class="field" style="left:92px;top:314px;width:385px">Telephone</div>
  <div class="field" style="left:92px;top:361px;width:385px">Code postal</div>
  <div class="field" style="left:92px;top:410px;width:182px">Nom</div>
  <div class="field" style="left:297px;top:410px;width:180px">Prenom</div>
  <div class="submit">Personalize Free Assesment &nbsp;→</div>
  <p class="fine">100% Free - Confidential - No Commitment</p>
  <div class="hero-art" role="img" aria-label="Isometric illustration of two advisors shaking hands beside a magnifying glass, stacks of banknotes and gold coins"></div>
</section>

<section class="advantages">
  <h2 class="section-title" style="top:76px">Tax exemption: the advantages of<br>investing in real estate</h2>
  <p class="section-lead" style="top:160px">With particularly low interest rates, and many existing tax systems, investing in rental property is one of the best solutions to reduce your taxes and meet many objectives.</p>

  <div class="card" style="left:92px;top:257px">
    <svg width="50" height="50" viewBox="0 0 50 50" fill="none" stroke="#1f66ae" stroke-width="2"><rect x="4" y="30" width="7" height="16"/><rect x="15" y="24" width="7" height="22"/><rect x="26" y="28" width="7" height="18"/><rect x="37" y="16" width="7" height="30"/><polyline points="6,22 18,14 28,18 42,4"/></svg>
    <h3>Reduce your taxes</h3><p style="top:58px">Up to 21% with the Pinel law, up to 30% on works with the Malraux law</p>
  </div>
  <div class="card" style="left:437px;top:257px">
    <svg width="50" height="50" viewBox="0 0 50 50" fill="none" stroke="#1f66ae" stroke-width="2"><circle cx="25" cy="25" r="21"/><circle cx="25" cy="18" r="6"/><path d="M14 38c3-8 19-8 22 0"/></svg>
    <h3>Build an estate</h3><p style="top:58px">Prepare your future and protect your loved ones</p>
  </div>
  <div class="card" style="left:784px;top:257px">
    <svg width="50" height="50" viewBox="0 0 50 50" fill="none" stroke="#1f66ae" stroke-width="2"><path d="M12 38L38 8l4 4-30 26z"/><circle cx="30" cy="20" r="4"/><path d="M8 44l6-6"/></svg>
    <h3>Optimizing your retirement</h3><p style="top:76px">By creating a monthly rent for your rental purchase</p>
  </div>
  <div class="card" style="left:92px;top:427px">
    <svg width="50" height="50" viewBox="0 0 50 50" fill="none" stroke="#1f66ae" stroke-width="2"><circle cx="27" cy="8" r="4"/><path d="M27 14l-4 14 8 8-4 10M23 28l-8 14M25 20l10 4"/><rect x="10" y="28" width="7" height="8"/></svg>
    <h3>Optimizing your savings</h3><p style="top:58px">With a return on property investment of 4 to 7%</p>
  </div>
  <div class="card" style="left:437px;top:427px">
    <svg width="50" height="50" viewBox="0 0 50 50" fill="none" stroke="#1f66ae" stroke-width="2"><path d="M6 44l10-10 8 2 14-14"/><circle cx="34" cy="12" r="8"/><rect x="14" y="22" width="10" height="8"/></svg>
    <h3>Additional income</h3><p style="top:58px">Finance your projects with your new rental income</p>
  </div>
  <div class="card" style="left:784px;top:427px">
    <svg width="50" height="50" viewBox="0 0 50 50" fill="none" stroke="#1f66ae" stroke-width="2"><path d="M8 24L25 10l17 14"/><rect x="12" y="24" width="26" height="18"/><rect x="21" y="30" width="8" height="12"/><circle cx="40" cy="10" r="5"/></svg>
    <h3>Become owner</h3><p style="top:58px">An opportunity to become an owner even without contribution</p>
  </div>
</section>

<section class="pinel">
  <h2 class="section-title" style="top:82px">€ 0 tax for 6, 9 or 12 years</h2>
  <p class="section-lead" style="top:130px;left:290px;width:620px;color:#888">Extended until 2022, the Pinel Law is one of the flagship devices in real estate investment because it is very tax-efficient.</p>

  <div class="chart-card">
    <svg class="abs" style="left:91px;top:34px" width="200" height="200" viewBox="-100 -100 200 200">
      <path d="M0,0 L0,-100 A100,100 0 0 1 96.9,-24.9 Z" fill="var(--pie-dark)"/>
      <path d="M0,0 L96.9,-24.9 A100,100 0 0 1 -84.4,53.6 Z" fill="var(--pie-pink)"/>
      <path d="M0,0 L-84.4,53.6 A100,100 0 0 1 0,-100 Z" fill="var(--pie-teal)"/>
      <g fill="#fff" font-size="14" font-family="Montserrat,sans-serif" text-anchor="middle">
        <text x="38" y="-50">21%</text><text x="10" y="45">45%</text><text x="-50" y="-22">34%</text>
      </g>
    </svg>
    <div class="legend" style="top:181px"><i style="background:var(--pie-dark)"></i>L'ÉTAT (réduction d'impôts)</div>
    <div class="legend" style="top:201px"><i style="background:var(--pie-pink)"></i>LE LOCATAIRE</div>
    <div class="legend" style="top:221px"><i style="background:var(--pie-teal)"></i>VOUS (effort d'épargne)</div>
    <p class="chart-caption">Comment est financé votre bien immobilier ?*</p>
  </div>
  <p class="footnote">* Example of financial breakdown for an investment over 12 years under Pinel law. 66% of the property is financed by the tenant and by the State. This is only an example, the share of the rent and the savings effort depending on many criteria: the Pinel area concerned and the surface area of the accommodation which will determine the rent ceiling, the debt capacity, the tax rate, the amount of investment.</p>

  <div class="focus">
    <div class="kicker">Focus on the Pinel law:</div>
    <h2>Up to € 63,000 in tax reduction!</h2>
    <p>This system allows the State to encourage the construction of new high-performance housing with supervised rent. In return for your investment, the State grants you tax advantages!</p>
    <p>For a rental of his property over 6 years you benefit from a tax reduction of 12%, over 9 years: 18%, over 12 years: 21% (maximum purchase price of 300,000 euros).</p>
    <span class="btn">Are you eligible for the Pinal Law?</span>
  </div>
</section>

<section class="testimonials">
  <h2 class="section-title">They benefited from our advice</h2>
  <p class="sub">These testimonials are from Avisly reviews</p>
  <p class="quote" style="left:138px;top:220px;width:250px">"We are very satisfied following an apartment bought in Pinel in the south of France with the Strasbourg agency."</p>
  <div class="quote-box"></div>
  <p class="quote" style="left:465px;top:200px;width:270px">"I have been advised of their services, so far I am very satisfied. They took the time to understand my needs, to explain everything to me, to anticipate my questions "</p>
  <div class="avatar" role="img" aria-label="Portrait photo of the reviewer"></div>
  <p class="author">Martin.D</p>
  <div class="dots"><i></i><i></i><i></i></div>
  <p class="quote" style="left:800px;top:220px;width:275px">"As far as I am concerned, I am satisfied with the advice of the regional director with whom I dealt. It is responsive, accessible and available. "</p>
</section>

<section class="group">
  <h2>A strong group, at the service of your heritage</h2>
  <p style="top:176px;width:470px">Created in 2009, the Valmoril Group operates in all sectors of Wealth Management:</p>
  <p style="top:228px">• Tax exemption &nbsp;• Wealth assessment an Investments</p>
  <p style="top:264px">• Financing</p>
  <div class="badge" style="left:93px;width:84px"></div>
  <div class="badge" style="left:190px;width:145px"></div>
  <div class="group-photo" role="img" aria-label="Photo of a delighted woman raising her fists in celebration"></div>
</section>

<div class="figure" style="left:92px">
  <svg width="42" height="40" viewBox="0 0 42 40" fill="none" stroke="#1f66ae" stroke-width="2"><path d="M2 12h14l4 4h20v22H2z"/><path d="M8 12V4h26v12"/></svg>
  <div><b>3800€</b><span>average tax saved / year</span></div>
</div>
<div class="figure" style="left:356px">
  <svg width="42" height="40" viewBox="0 0 42 40" fill="none" stroke="#1f66ae" stroke-width="2"><path d="M2 34l10-8h12l8-6M2 38h30"/><circle cx="22" cy="10" r="6"/><path d="M22 0v3M30 4l-2 2M14 4l2 2"/></svg>
  <div><b>50Millions €</b><span>average tax saved / year</span></div>
</div>
<div class="figure" style="left:608px">
  <svg width="36" height="40" viewBox="0 0 36 40" fill="#1f66ae"><circle cx="16" cy="10" r="8"/><path d="M2 36c0-12 6-16 14-16s14 4 14 16z"/><path d="M28 30h8M32 26v8" stroke="#1f66ae" stroke-width="2"/></svg>
  <div><b>250</b><span>employees throughout France</span></div>
</div>
<div class="divider"></div>

<div class="value-pill">Our value</div>
<p class="section-lead" style="top:3164px;left:340px;width:520px;font-size:13px;color:#777">Whatever the composition of your heritage and your personal situation, you are committed to protecting what you have acquired and ensuring that this heritage can be appreciated over time. The Valmoril Group deploys all the expertise to help you.</p>

<div class="value-card" style="left:92px;background:linear-gradient(120deg,#1f5fc4,#3381e0)"><h3>Expertise</h3><p>Professional advisers in the sector with certified training</p></div>
<div class="value-card" style="left:349px;background:linear-gradient(120deg,#1eb98a,#2ad6a3)"><h3>Proximity</h3><p>A heritage advisor, attentive and close to you</p></div>
<div class="value-card" style="left:606px;background:linear-gradient(120deg,#1e88c8,#2fa6e3)"><h3>Independence</h3><p>We do not depend on any third party (bank, insurance, promoter ...)</p></div>
<div class="value-card" style="left:861px;background:linear-gradient(120deg,#e21f5a,#f0582a)"><h3>Satisfaction</h3><p>The recommendations of our customers are our 1st source of turnover</p></div>

<footer class="site-footer">
  <div class="contact" style="left:158px">
    <svg width="26" height="26" viewBox="0 0 26 26" fill="none" stroke="#555" stroke-width="1.5"><circle cx="13" cy="13" r="12"/><path d="M9 7l3 3-2 2c1 2 2 3 4 4l2-2 3 3-2 2c-4 0-10-6-10-10z"/></svg>
    Tel: +33 (0)1 45 00 12 34
  </div>
  <div class="contact" style="left:466px">
    <svg width="26" height="20" viewBox="0 0 26 20" fill="none" stroke="#555" stroke-width="1.5"><rect x="1" y="1" width="24" height="18"/><path d="M1 1l12 10L25 1"/></svg>
    contact@groupe-valmoril.fr
  </div>
  <div class="social"><i></i><i></i><i></i><i></i></div>
  <p class="legal">The information collected from the form on our site is subject to computer processing intended for the Valmoril Group. In accordance with article 34 of the law "computing and liberties" of January 6, 1978, you have a right of access and of correction to the information which concerns you. You can access your information by contacting cnil@groupe-valmoril.fr. You can also, for legitimate reasons, oppose the processing of data concerning you. To find out more, consult your rights on the CNIL website.</p>
  <div class="to-top"><svg width="54" height="54" viewBox="0 0 54 54" fill="none" stroke="#fff" stroke-width="3"><path d="M27 38V16M19 24l8-8 8 8"/></svg></div>
</footer>

</body>
</html>
```